Label Design

Our company is looking for someone to design a label for our juice bottles. We need 1 design that can be edited and used for four different juice combinations. We are a local juice shop that sales fruit and vegetable juices. We would like to see designs that outline the name of the juices, ingredients included within the juice, and size of the bottle. The dimensions of our bottles are 9.67 inches height x 1.97inches width. We are looking for something that is simple yet eye catching.

```html
<!DOCTYPE html>
<html lang="en">
<head>
<meta charset="utf-8">
<title>Reviving Ruby – Juice Label</title>
<link href="https://fonts.googleapis.com/css2?family=Baloo+2:wght@700;800&family=Russo+One&display=swap" rel="stylesheet">
<style>
  :root {
    --page-bg: #f3efea;
    --peach-light: #fbe3d6;
    --peach-mid: #f6c3ad;
    --label-red: #ea1f2c;
    --label-red-dark: #c9141f;
    --brand-red: #e3222c;
    --white: #ffffff;
    --rule: rgba(255,255,255,0.45);
  }
  * { margin: 0; padding: 0; box-sizing: border-box; }
  html, body { width: 1200px; height: 934px; overflow: hidden; background: var(--page-bg); }
  .canvas { position: relative; width: 1200px; height: 934px; }

  .label {
    position: absolute;
    left: 508px; top: 18px;
    width: 184px; height: 898px;
    overflow: hidden;
    background: linear-gradient(180deg, var(--peach-mid) 0%, var(--peach-light) 45%, var(--peach-mid) 75%);
  }

  .brand {
    position: absolute;
    left: 92px; top: 152px;
    width: 240px;
    transform: translate(-50%, -50%) rotate(-90deg);
    text-align: center;
    font-family: "Baloo 2", sans-serif;
    font-weight: 800;
    font-size: 36px;
    line-height: 34px;
    color: var(--brand-red);
    white-space: nowrap;
  }
  .brand span { display: block; }

  .hero-art {
    position: absolute;
    left: 0; top: 262px;
    width: 184px; height: 380px;
    background: radial-gradient(ellipse 55% 50% at 50% 50%, #e8463b 0%, #ef6c5a 45%, rgba(246,195,173,0) 80%);
  }

  .info-panel {
    position: absolute;
    left: 0; top: 660px;
    width: 184px; height: 238px;
    color: var(--white);
    text-align: center;
  }
  .info-panel .wave { position: absolute; left: 0; top: 0; width: 184px; height: 40px; }
  .info-body {
    position: absolute; left: 0; top: 30px; width: 184px; bottom: 0;
    background: var(--label-red);
  }
  .flavour {
    position: absolute; left: 0; right: 0; top: 16px;
    font-family: "Russo One", sans-serif;
    font-weight: 400;
    font-size: 24px; line-height: 25px; letter-spacing: 1px;
  }
  .rule { position: absolute; left: 10px; right: 10px; height: 1px; background: var(--rule); }
  .rule.first { top: 76px; }
  .rule.second { top: 128px; }
  .juice-type {
    position: absolute; left: 0; right: 0; top: 80px;
    font-family: "Baloo 2", sans-serif; font-weight: 800; font-size: 14px; line-height: 18px;
  }
  .ingredients {
    position: absolute; left: 0; right: 0; top: 101px;
    font-family: "Baloo 2", sans-serif; font-weight: 700; font-size: 10px; line-height: 12px;
  }
  .storage {
    position: absolute; left: 0; right: 0; top: 134px;
    font-family: "Baloo 2", sans-serif; font-weight: 700; font-size: 10px; line-height: 15.5px;
  }
  .volume {
    position: absolute; left: 0; right: 0; bottom: 0; height: 24px;
    background: var(--label-red-dark);
    font-family: "Baloo 2", sans-serif; font-weight: 800; font-size: 12px; line-height: 25px;
  }
</style>
</head>
<body>
<main class="canvas">
  <section class="label">
    <div class="brand"><span>Radiant</span><span>PRESSERY</span></div>

    <div class="hero-art" role="img" aria-label="Illustration of watermelon slices, apple, cucumber and basil leaves in a swirling red juice splash"></div>

    <div class="info-panel">
      <svg class="wave" viewBox="0 0 184 40" preserveAspectRatio="none" aria-hidden="true">
        <path d="M0 14 C40 0 70 2 92 12 C114 22 150 4 184 8 L184 40 L0 40 Z" fill="#ea1f2c"/>
      </svg>
      <div class="info-body">
        <h1 class="flavour">REVIVING<br>RUBY</h1>
        <div class="rule first"></div>
        <p class="juice-type">Fruit &amp; Vegetable Juice</p>
        <p class="ingredients">Apple | Basil | Watermelon |<br>Zucchini</p>
        <div class="rule second"></div>
        <p class="storage">Keep Refrigerated &amp; Shake well<br>Perishable, Not pasteurized<br>Drink/Freeze by</p>
        <p class="volume">12 FL OZ (355ML</p>
      </div>
    </div>
  </section>
</main>
</body>
</html>
```